New website for Scuba Diving School ‘FinWaveX’ in Dublin, Ireland

New website for Scuba Diving School ‘FinWaveX’ based in Dublin, Ireland.

GENERAL DESCRIPTION OF WHAT I WANT THIS WEBSITE TO BE:

Website must be professional and modern looking. It has to be user friendly so that everybody can easily find information they are looking for. I would like to see the site being innovative and funky yet still appeal to the main market which is 25-35 years old with 2/3 being male middle to high income.

Site should be creative with bright colours. As the site is for scuba diving school it should be cheerful and welcoming. Colours should be eye catching and worm to create friendly image from a very first time it’s visited. Images used in the website should stay as realistic as possible yet professional.

Home Page:
Section 1) Left up to you if you want anything above the menu bar.

Section 2) Under need I want to have menu bar that will have 6 main pages and 6 subpages. How you designed the menu bar is up to you as long as you stick the correct content:

Main Page 1. Home
Main Page 2. About Us
Main Page 3. Courses & Prices
Sub Page - Try a Dive Evening
Sub Page - Scuba Review
Sub Page - Beginners Course
Sub Page - Advanced Open water
Sub Page - Rescue Diver
Sub Page - DiveMaster Course
Main Page 4. Contact Us
Main Page 5. FAQ
Main Page 6. Calendar

Section 3)
I would like to stick to minimum text content on the main page but I would like to see the following:

Under the menu bar please create an image slide show that will change every couple of seconds or can be operated by user when clicked on dot, number or arrow. Example can be found on the fallowing website: http://www.brightgrid.example/?tv or http://www.norva.example/scuba/ this is just to give you an idea. I want this slide show to be creative and promote all courses one by one. Pictures in the slide show must be relevant and professional. On each slide please use exact content provided below:

- 1st slide. Content: "Try a Dive Evening for ONLY 49€'
- 2nd slide Content: “Sign up Today for your Beginners Course"
- 3rd slide Content: "Norva Advanced Diver Course"
- 4th slide Content: "The Norva Rescue Diver Course"
- 5th slide Content: "SnapFin with Norva DiveMaster course"

Please link those slides with appropriate course pages so the user can be redirected directly to the course page.

Section 4)
On the bottom of the page I would like to see all links in columns in small print with my logo in the right bottom corner. Please make the logo clearly visible

ADDITIONAL INFORMATION:

Also, somewhere on the page I would like to see some form of a price tag that will attract user attention. The purpose of this price tag is for the user to click on it to check our discounts.

Content for the Price Tag: “MATES RATES 10%OFF” and when clicked it will bring up a pop up window that will state the following:
POP UP Content:

“Sign up now for our next "Try a Dive Evening" and get 10% when you come with your friend! Bring two friends and get 10% off of your next Beginners course"!
Contact us now to book your place!

‘Contact us’ should be a link that will redirect user to the ‘Contact Us’ Page. (This should be done on all pages) plus the link to the calendar page.

About us Page:

Section 1 and Section 2 from the home page should be repeated.

Section 3) Content:

This section will be information to give a customer overview of who we are and what we do. I will provide you with the picture in the next 3-4 day (waiting for the photographer to get back to me) which I would like to be included on this page with fallowing information: Tomas Kelvry Norva No. 584731.
Also I would like this picture to be part of the fallowing content:
Please stick to exact wording:

Content:
Welcome to FinWaveX

We are Dublin based scuba diving school dedicated to teaching Scuba Diving in the internationally recognised NORVA diving system. We have a real passion for diving and love everything about the real magic that the underwater world has to offer.

We teach a range of courses starting from a very beginning right through to professional level diving. All our staffs are official Scuba Diving NORVA, MLS instructors and NORVA DiveMasters.

We take great pride in our professional approach to diving and can guarantee that that you will receive the highest level of expertise and attention available whether you are trying just one evening of scuba or completing your Dive Master program.

FinWaveX is a progressive Eco minded business promoting safe and responsible diving. In everything we do. Everybody who learns to scuba dive with us is taught that safety is at the heart of everything we do in Scuba. The whole worlds of the oceans are opened up to be discovered. We believe that we can all make a huge difference in keeping our oceans healthy and self-sustaining for the generations to come.

Meet our owner and NORVA qualified Instructor at FinWaveX.

“I am originally from Poland but moved to Ireland in 2006 and yes I have a Dublin accent now! When I started my adventures in diving here was keen to explore the wonders of many of great diving sites in Irelands surrounding coastline. I am a professionally qualified Norva Open Water Instructor and I really enjoy working with students on all levels. I have a genuine love and passion for the Irish waters and from the beginning when I sold my car to purchase my first diving equipment I knew this is the path in life that I want to take. I LOVE THE WATER! Most people probably don’t know that Ireland is one of the best places in the world for scuba diving. The diversity of marine life on Ireland’s coasts is absolutely fantastic. Now that we have a great Riverside Swim Complex we have unrivalled facilities for people to start with scuba in the controlled surroundings before moving on to discover the great underwater world in the seas. I encourage everybody to give it a go and discover for themselves what turned my world upside down”.

Section 4)

Courses Page

Section 1 and Section 2 from the home page should be repeated on each course page. I don’t want all courses on one page that’s why I listed them as subpages in form of a dropdown menu. I want the customer to have a choice where they go so they can skip the information that is not relevant to them.

Please stick to the exact content provided below. Please use some images on each of the course pages to reflect the information provided for the customer. Again please make the images smaller so they add to the page and not still attention from the text.

Furthermore, please call each page in the drop down menu as you can see them in Section 2 of the home page.

• Subpage 1 ‘Try a Dive’
Content:
Discover Scuba Diving (Price Tag: Only 49€)
Have you ever seen those underwater documentaries and wish you could discover the amazing world of scuba for yourself? Or have you ever watched a scuba diver on TV and wondered if you could ever experience the fascinating world that exists under the sea? Or did you know Ireland has some of the most fascinating and diverse marine ecosystems in the world and they are right on our door step? Well now you can easily discover scuba for yourself in the comfort of the world class facilities at Dublin’s Riverside Swim Complex under the direction and supervision of a FinWaveX Scuba Instructor.

This Discover Scuba Diving Norva program is a great introduction to the magical world of scuba. In the comfort of the swimming pool under watchful eye of your instructor you will get a chance to learn a few basics about scuba diving, practice some fun skills and familiarise yourself with scuba equipment

There is no need for previous experience or the ability to swim like an Olympian. You just need a towel and a swimsuit and we provide you with the rest.
Our Discover Scuba Diving night happens on Tuesday evenings 7-10pm using the facilities at the Riverside Swim Complex.

It really is that simple so don’t wait any longer!

Contact us today to book your adventure now.

• Subpage 2 ‘Scuba Review’
Content:
Scuba Review (Price Tag: Only 59€)
If it been a while since you had a chance to dive with your buddy and your skills are a bit rusty or maybe you thinking of doing some scuba again on holiday then why not take part in this scuba review program to refresh your skills at the Riverside Swim Complex

Norva Scuba Review was designed for anybody who is certified but has stopped diving for a while and would like to get back into the sport again .During this one- evening session our instructor will review your diving knowledge and help you practice your skills before you head back to the open water.

There is no requirement to take the full theory test again.

Simply contact us to complete your Scuba Review!

• Subpage 3 ‘Beginners Course’
Content:
Open Water Diver (Price Tag: Only 559€)
The NORVA Open Water course opens the door of a whole new world of discovery. Everything that happens underwater from discovering our amazing diverse marine life to diving to see long lost ship wrecks all begins with completing your first Open Water course. Once you have completed this course you will be awarded your own internationally recognized scuba diving license which allows you to explore the wonderful world of scuba on any future holidays or international travels.

If you've always wanted to learn how to scuba dive, this course is the best way to start. The NORVA Open Water Diver course is the world's most popular scuba course, and has introduced millions of people to the adventurous diving lifestyle.

Breathing under water for the first time is something new and unforgettable. Our Norva Open Water course is structured in a way that allows you to study at your own comfortable pace. The course teaches you the scuba diving theory behind diving, and allows you to practice your diving skills in the comfort of the swimming pool in the world class facility of the Riverside Swim Complex. We will then take you out into the sea for your open water dives to allow you practice your new scuba diving skills under our professional supervision.

We designed our courses to fit your busy life style. Our classroom and pool training takes place every Tuesday in Riverside Swim Complex from 7 to 10 pm. Once you have enough knowledge of the scuba diving basics completed in the pool we will then take you diving in the open water at one of the great local dive sites. We offer a high degree of flexibility to people completing the course and if you do miss some classes we schedule extra time at no extra cost to allow your course completion.

Our course runs over a period of six weeks. Five evening’s sessions in the pool and one weekend at one of our regular dive sites.

What you need is a towel and a swimsuit the rest will be provided.
You can start your Open Water Diver course today by simply getting in touch with us by clicking on Contact us.

• Subpage 4 ‘Advanced Open water’
Content:
Advanced Open Water Diver (Price Tag: Only 389€)

Keeping your diving skills sharp is an important part of scuba diving. Once you have completed your Open Water scuba course and begin to feel comfortable with your dives then you may decide you wish to learn additional diving skills, undertake some deeper dives and further develop your knowledge of scuba diving. Our Advance Open Water Course is specially designed for this purpose.

This course is structured in a way that enables you to learn more about the various different types of diving. It includes 5 great adventure dives that will allow you maximize the enjoyment of your diving skills and as safety is always our priority the course is completed under the guidance of our experienced qualified FinWaveX instructor.
This course involves some theory without the need for final exam so you will have more time to enjoy some of our awesome dive sites.

This course is only suitable if you have already completed your NORVA Open Water Diver (or qualifying certification from another training organization). But remember You don't need to have your own diving equipment as FinWaveX will provide everything you need for course participation.

The course is conducted over one weekend and we run advanced courses regularly all year round. If you can't make it on the weekends we can also run it during the week.
You can start your Advanced Open Water Diver course today by simply getting in touch with us by clicking on Contact us.

• Subpage 5 ‘Rescue Diver’
Content:
Rescue Diver (Price Tag: Only 369€)

Scuba diving is one of the most enjoyable and fulfilling activities experienced by thousands of people around the world every day. The popularity of recreational diving continues to increase every year. The diving community places safety as our number one primary concern for all participants in the sport.

The Norva Recue Diver program is designed to teach you the skills and give you the appropriate training which can help prevent emergency situations to occur. You will also receive training on the best practices required to help manage an emergency situation. Certified Norva Rescue Divers look back on their rescue training as one of the most challenging – sometimes demanding- and therefore one of the most rewarding programs they’ve taken.

If you dive very often then eventually you may find yourself in a situation where you, your buddy or a fellow diver may need some help or assistance. This course teaches you the skills and knowledge required to take control of a rescue situation.

If you are thinking of working towards further professional ratings such as DiveMaster then this is a valuable step along the way.

To participate in this course you must have a current first aid & CPR certificate and have completed a NORVA Advanced Open Water Diver (or a similar qualifying rating) prior to starting the Rescue course.

The course is combined with class room and pool training in the Riverside Swim Complex and open water training is completed at one of our dive sites.

If you are interested in our Norva Rescue diver program then Contact us here...

• Subpage 6 ‘DiveMaster Course’
Content:
DiveMaster Program (Price Tag: Only 559€)

If you are really serious about your scuba diving then you should consider qualifying as a NORVA DiveMaster with FinWaveX. The NORVA DiveMaster course is the first level of the NORVA Professional ratings. As a NORVA DiveMaster you will hold the minimum rating for employment in the diving industry. Your qualification will allow you to supervise recreational diving activities (either boat or land based), work as an Instructional assistant on all NORVA courses and is just one step away from a NORVA Instructor rating.

Working closely with a NORVA Instructor, in this program you expand your dive knowledge and hone your skills to the professional level. NORVA DiveMaster training develops your leadership abilities, qualifying you to supervise dive activities and assist instructors with student divers. NORVA DiveMaster is the prerequisite certification for both the NORVA Assistant Instructor and NORVA Open Water Scuba Instructor certifications.

After successfully completing your DiveMaster course you will earn the title of DiveMaster and be authorized to:
• Supervise both training and non-training-related activities by planning, organizing and directing dives
• Assist a NORVA Instructor during the training sessions for any NORVA Diver course
• Conduct the NORVA Skin Diver course and NORVA Discover Snorkelling program
• Conduct the NORVA Discover Local Diving experience
• Conduct the NORVA Scuba Review program
• If qualified as a Discover Scuba Diving Leader, independently conduct the NORVA Discover Scuba Diving program.
• Earn the NORVA Digital Underwater Photographer Specialty Instructor rating to be able to teach the NORVA Digital Underwater Photographer specialty.
• Independently guide Open Water Diver course students on the tour portion of Open Water Diver course Training Dives 2, 3 and 4 at a ratio of two student divers per certified DiveMaster.
• Accompany Open Water Diver students under the indirect supervision of a NORVA Instructor during:
o surface swims to and from the entry/exit point and during navigational exercises
o when the instructor conducts a skill, such as an ascent or descent, a DiveMaster can remain with other student divers (with an individual student or buddy team)
• Accompany student divers during Adventure Dives or Specialty training dives under the indirect supervision of a NORVA Instructor.
• Conduct the NORVA Otter Crew Skin Diver Specialist TideQuest
• Conduct subsequent dives under an instructor’s indirect supervision for Discover Scuba Diving participants after participants have satisfactorily completed the first dive with a NORVA Instructor.
• Teach Medic Lifeline Support courses after successfully completing an Medic Lifeline Support Instructor course.

You also gain access to exclusive Norva Pro site with many benefits such as Job forums for dive professionals.

To complete this course there are some minimum requirements you must be:

• 18 years old and NORVA Advanced Open Water Diver (or qualifying certification from another training organization
• A NORVA Rescue Diver (or qualifying certification from another training organization)
• An Medic Lifeline Support Primary and Secondary Care (or qualifying first aid and CPR training from another organization) course completion within the past 24 months.
• Have at least 40 dives to begin the course and 60 for certification
• Be fit for diving and submit a Medical Statement signed by a physician within the last 12 months.
• Have your own equipment
What can you expect completing your NORVA DiveMaster with FinWaveX?
FinWaveX manage the qualification process as a DiveMaster with a very high degree of personal teaching. We are not a high volume ‘factory style ‘diving school. We offer a personal friendly environment encouraging you to develop your diving skills in an enjoyable way. Typically we will only enrol a maximum of 3 interns at one time. We ensure to offer very thorough training and our goal is to make you an employable, experienced member of the worldwide professional diving community.

You will be “immersed” in the world of scuba diving. In addition to your learning you also will be working alongside your instructor during all recreational level courses so you can learn how a run courses, coordinate dive trips, supervise divers in the water and learning your own teaching skills.

To be awarded as Norva DiveMaster you will need to complete and pass fallowing:
• Complete knowledge development sessions and pass the DiveMaster final exam
• Create an Emergency Assistance plan
• Complete waters kills exercises
• Complete a diver rescue assessment
• Complete the dive skill workshop and assessment
• Complete practical application skills
• Complete DiveMaster-conduct programs workshop
• Complete practical assessment
As you can see the NORVA DiveMaster program with FinWaveX is a very comprehensive diving program suitable for anyone who is enthusiastic or serious about Scuba Diving. The program usually takes between 3 and 6 months to complete. If you interested in finding out more about qualifying as a Norva DiveMaster with FinWaveX then simply contact us and we will discuss the process and answer any questions you may have.

What are the total costs involved in the DiveMaster Program?

The NORVA DiveMaster Program with FinWaveX costs 559€.Fees can be payable in instalments over the course of the program. Your NORVA DiveMaster crew pack will cost 180€.
If you are interested in completing your Norva DiveMaster program contact us and a FinWaveX Diving Instructor will be happy to answer any questions you may have.

Section 4)

Contact us Page:

Section 3)
This section is the ‘contact’ form. The actual image of the contact for is left up to you but please create the form so I can receive the fallowing information:

Name
E-mail address
Contact Number
Text (2000 symbol minimum so user can send us email without the need of contacting us twice)

Under need please add Mapzy map that will allow users to locate the Riverside Swim Complex in Dublin, Ireland.

Section 4)

FAQ Page

Section 3) those are actual questions and answer that I would like to see:

Q Who can do scuba diving?
A: Anyone in good health can do scuba diving.

Q Do I have to pay all my fees upfront for courses?
A. For open water diver and above we only require a 20% deposit on the first night and the rest can be paid over the period of your course

Q I don’t have any scuba equipment is this a problem?
A: No, all your equipment will be provided for you by us

Q Do I need to consider insurance to go scuba diving with FinWaveX?
A: No, all our students are covered by our insurance

Q. Where do I purchase books for the scuba courses you offer?
A All your Norva Studding Materials will be supplied by us

Q If I am unable to dive due to illness do I miss out on my course?
A No, if you miss a course dive we simply schedule extra time at no extra cost

Q Is the Irish weather a major problem ?
A The great thing about discovering Scuba with us is that all our intimal training is at the indoor facilities at the Riverside Swim Complex. For your safety and comfort we always reschedule open water dives for suitable weather conditions

Q Can I take exams in my native language?
A Yes study material are available in all languages, just inform us before you start your course.

Q Can I go diving without the appropriate training?
A No, for safety you are required to complete training course before diving.

Section 4)

Calendar Page:

Section 3)
I would like to have active calendar which I can update myself so that users can see upcoming courses:

Please make sure that calendar is active and that current date in highlighted. I don’t want the user to be under the impression that our calendar is simple copy past picture.
Due to unpredictable weather patterns in Ireland I need to be able to update calendar myself.

Section 4)

Addition Information: In the next couple of months (2-4) I would like to add few subpages to this website to promote more diving courses. So there will be a chance of extra income for the person who will design this site.

If you need any more information feel free to contact me.

Kind Regards and Thanks to all of you for taking on this project.
Tomas Kelvry
Updates

Hello,

First of all I would like to say massive thanks for all work so far and I would like to apologize for not attaching my logo to my brief. I just corrected this so you have access to it.

Thanks,
Tomas Kelvry

Target Market(s)

basics statistics can be found: http://www.norva.example/scuba/about-norva/norva-statistics/Default.aspx

Industry/Entity Type

Progressive

Requirements
Must have
• Active calendar so i can update courses myself
Nice to have
• maybe date and clock in the corner just for esthetic apperance
Should not have
• complicated layout or menu bar that is not practical and clearly visible

```html
<!DOCTYPE html>
<html lang="en">
<head>
<meta charset="utf-8">
<title>FinWaveX – Scuba Diving School Dublin</title>
<link href="https://fonts.googleapis.com/css2?family=PT+Sans:wght@400;700&family=Oswald:wght@500&family=Varela+Round&display=swap" rel="stylesheet">
<style>
:root{
  --sky:#2fb8f0;
  --nav-dark:#14304a;
  --nav-text:#3ab8f0;
  --sea-top:#1a8fd8;
  --sea-mid:#1470c8;
  --sea-deep:#0c4fa8;
  --footer:#0d3a78;
  --white:#ffffff;
  --drop:rgba(18,48,70,.9);
  --drop-link:#4cc4f5;
  --tile-band:rgba(10,30,50,.75);
  --orange:#f7a21b;
  --orange-light:#fbc54a;
  --orange-dark:#e08410;
  --yellow-top:#ffe03a;
  --yellow-bot:#f2b705;
  --btn-text:#c85a00;
  --digit:#3a3d40;
}
*{margin:0;padding:0;box-sizing:border-box}
html,body{width:1200px;height:1125px;overflow:hidden;background:var(--sea-deep)}
.page{
  position:absolute;left:0;top:0;width:1280px;height:1200px;
  transform:scale(.9375);transform-origin:0 0;
  font-family:"PT Sans",sans-serif;color:var(--white);
}
.ocean-backdrop{
  position:absolute;inset:0;
  background:
    radial-gradient(ellipse at 70% 20%,rgba(120,220,255,.45),transparent 55%),
    radial-gradient(ellipse at 10% 85%,rgba(40,110,190,.6),transparent 50%),
    linear-gradient(180deg,var(--sea-top) 0%,var(--sea-mid) 55%,var(--sea-deep) 100%);
}
/* header */
.site-header{position:absolute;left:0;top:0;width:1280px;height:100px;background:linear-gradient(90deg,#1b3a55,#24506e 50%,#1c3d58)}
.brand{position:absolute;left:0;top:0;width:440px;height:100px;background:var(--sky)}
.brand-name{position:absolute;left:160px;top:24px;font-size:46px;font-weight:700;color:var(--white);letter-spacing:.5px}
.main-nav a{position:absolute;top:30px;height:40px;line-height:40px;width:110px;text-align:center;font-size:14px;color:var(--nav-text);text-decoration:none}
.main-nav a.is-active{background:var(--sky);color:var(--white);border-radius:3px}
.nav-caret{position:absolute;left:728px;top:70px;width:0;height:0;border-left:7px solid transparent;border-right:7px solid transparent;border-top:8px solid var(--nav-text)}
.dropdown{position:absolute;left:680px;top:100px;width:180px;height:180px;background:var(--drop);z-index:5}
.dropdown a{display:block;height:30px;line-height:30px;padding-left:20px;font-size:13px;color:var(--drop-link);text-decoration:none}
.dropdown a:first-child{color:var(--white)}
/* slider */
.slider{position:absolute;left:160px;top:130px;width:960px;height:420px;background:var(--white);border-radius:30px}
.slide-photo{position:absolute;left:10px;top:10px;width:940px;height:400px;border-radius:22px;
  background:radial-gradient(ellipse at 60% 30%,#4fd0ff,#1a9ae6 55%,#0d74c8)}
.slide-title{position:absolute;left:50px;top:237px;font-size:35px;font-weight:700;white-space:nowrap}
.slide-sub{position:absolute;left:49px;top:278px;font-size:23px;font-weight:700;white-space:nowrap}
.signup-btn{position:absolute;left:50px;top:325px;width:218px;height:52px;border-radius:5px;
  background:linear-gradient(var(--yellow-top),var(--yellow-bot));box-shadow:0 3px 4px rgba(0,0,0,.25);
  font-family:"Oswald",sans-serif;font-size:26px;color:var(--btn-text);text-align:center;line-height:52px;text-decoration:none}
.slide-dots{position:absolute;left:856px;top:376px;display:flex;gap:6px}
.slide-dots span{width:14px;height:14px;border-radius:50%;background:#1c6fa8}
.slide-dots span.on{background:var(--white)}
/* welcome */
.section-title{position:absolute;font-size:29px;font-weight:700;white-space:nowrap}
.welcome-text{position:absolute;left:158px;top:616px;width:635px;font-size:13px;line-height:18px}
.welcome-text p+p{margin-top:18px}
.course-tile{position:absolute;width:200px;height:140px;border:2px solid #dfe8ee;border-radius:6px;overflow:hidden;
  background:linear-gradient(160deg,#5fc7e8,#1e88b8 60%,#135f88);color:var(--white);text-decoration:none}
.course-tile .photo{position:absolute;inset:0}
.course-tile .label{position:absolute;left:0;bottom:0;width:100%;height:38px;line-height:38px;background:var(--tile-band);
  text-align:center;font-size:15px;font-weight:700;text-transform:uppercase;color:var(--white);white-space:nowrap}
/* calendar */
.calendar{position:absolute;left:820px;top:625px;width:300px;height:294px;border:3px solid #ffe9b8;border-radius:6px;background:var(--orange);font-family:"Varela Round",sans-serif}
.cal-head{position:absolute;left:12px;top:3px;width:270px;height:42px;background:linear-gradient(#ffd35a,var(--orange));text-align:center;line-height:42px;font-size:18px}
.cal-arrow{position:absolute;top:18px;font-size:12px;color:#ffe9b8}
.cal-days{position:absolute;left:0;top:46px;width:294px;height:28px;background:var(--orange-dark);display:grid;grid-template-columns:repeat(7,1fr);text-align:center;line-height:28px;font-size:16px;color:#ffe08a}
.cal-grid{position:absolute;left:12px;top:87px;display:grid;grid-template-columns:repeat(7,36px);grid-auto-rows:29px;gap:2.5px 2.5px;font-size:16px;text-align:center}
.cal-grid span{background:var(--orange-light);line-height:29px;color:#3a2a10}
.cal-grid span.muted{color:#fff3d0}
.cal-grid span.event{color:var(--white);font-weight:700}
.cal-grid span.today,.cal-grid span.marked{background:var(--white);position:relative}
.cal-grid span.today::after{content:"";position:absolute;right:2px;bottom:2px;border-left:6px solid transparent;border-bottom:6px solid #e0261a}
/* countdown */
.countdown{position:absolute;left:835px;top:950px;width:272px;height:86px;border-radius:4px;background:linear-gradient(#f2f4f5,#b9bec2);box-shadow:0 2px 4px rgba(0,0,0,.3)}
.countdown-inner{position:absolute;left:6px;top:6px;width:260px;height:74px;background:linear-gradient(#d5d9dc,#a9afb3);border-radius:3px}
.digit{position:absolute;top:6px;width:68px;height:62px;background:linear-gradient(#5a5e62,var(--digit));border-radius:4px;font-family:Arial,sans-serif;font-weight:700;font-size:36px;text-align:center;line-height:62px;color:var(--white)}
.colon{position:absolute;top:27px;font-weight:700;color:#333;font-size:18px}
.count-labels span{position:absolute;top:1048px;font-size:13px;width:80px;text-align:center}
/* footer */
.site-footer{position:absolute;left:0;top:1100px;width:1280px;height:100px;background:var(--footer)}
.footer-links{position:absolute;left:160px;font-size:11px;color:#e6eefb;white-space:nowrap}
.footer-links a{color:#e6eefb;text-decoration:none}
.footer-links i{font-style:normal;margin:0 9px}
.copyright{position:absolute;left:160px;top:68px;font-size:11px;color:#e6eefb}
.social{position:absolute;top:36px;width:28px;height:28px;border-radius:50%;background:#dfe7f0;border:2px solid #9fb4cc}
</style>
</head>
<body>
<div class="page">
  <div class="ocean-backdrop" role="img" aria-label="Underwater background with coral, fish and a ray"></div>

  <header class="site-header">
    <div class="brand"><span class="brand-name">FinWaveX</span></div>
    <nav class="main-nav">
      <a class="is-active" style="left:460px" href="#">Home</a>
      <a style="left:570px" href="#">About</a>
      <a style="left:680px" href="#">Courses &amp; Prices</a>
      <a style="left:790px" href="#">Contact</a>
      <a style="left:900px" href="#">FAQs</a>
      <a style="left:1010px" href="#">Calendar</a>
    </nav>
    <span class="nav-caret"></span>
  </header>

  <div class="dropdown">
    <a href="#">Try a Dive Evening</a>
    <a href="#">Scuba Review</a>
    <a href="#">Beginners Course</a>
    <a href="#">Advanced Open water</a>
    <a href="#">Rescue Diver</a>
    <a href="#">DiveMaster Course</a>
  </div>

  <section class="slider">
    <div class="slide-photo" role="img" aria-label="Photo of scuba divers swimming in clear blue water"></div>
    <div class="slide-title">Try a Dive Evening for ONLY 49€</div>
    <div class="slide-sub">Sign up Today for your Beginners Course</div>
    <a class="signup-btn" href="#">SIGN UP NOW!</a>
    <div class="slide-dots"><span class="on"></span><span></span><span></span><span></span></div>
  </section>

  <h2 class="section-title" style="left:159px;top:573px">Welcome to our Site</h2>
  <div class="welcome-text">
    <p>We are Dublin based scuba diving school dedicated to teaching Scuba Diving in the internationally recog-nised NORVA diving system. We have a real passion for diving and love everything about the real magic that the underwater world has to offer.</p>
    <p>We teach a range of courses starting from a very beginning right through to professional level diving. All our staffs are official Scuba Diving NORVA, MLS instructors and NORVA DiveMasters.</p>
  </div>

  <a class="course-tile" style="left:160px;top:765px" href="#"><span class="photo" role="img" aria-label="Photo of divers in a pool"></span><span class="label">Try a Dive Evening</span></a>
  <a class="course-tile" style="left:375px;top:765px" href="#"><span class="photo" role="img" aria-label="Photo of two divers underwater"></span><span class="label">Scuba Review</span></a>
  <a class="course-tile" style="left:590px;top:765px" href="#"><span class="photo" role="img" aria-label="Photo of an instructor with a young diver"></span><span class="label">Beginner Course</span></a>
  <a class="course-tile" style="left:160px;top:920px" href="#"><span class="photo" role="img" aria-label="Photo of a diver by a coral reef"></span><span class="label">Advanced Open Water</span></a>
  <a class="course-tile" style="left:375px;top:920px" href="#"><span class="photo" role="img" aria-label="Photo of a rescue exercise in water"></span><span class="label">Rescue Diver</span></a>
  <a class="course-tile" style="left:590px;top:920px" href="#"><span class="photo" role="img" aria-label="Photo of a diver hovering in open water"></span><span class="label">Dive Master Course</span></a>

  <h2 class="section-title" style="left:820px;top:573px">Upcoming Events</h2>
  <div class="calendar">
    <div class="cal-head">April 2013</div>
    <span class="cal-arrow" style="left:4px">&#8249;</span>
    <span class="cal-arrow" style="right:4px">&#8250;</span>
    <div class="cal-days"><span>Su</span><span>Mo</span><span>Tu</span><span>We</span><span>Th</span><span>Fr</span><span>Sa</span></div>
    <div class="cal-grid">
      <span class="muted">25</span><span class="muted">26</span><span class="muted">27</span><span class="muted">28</span><span class="muted">29</span><span class="muted">30</span><span>1</span>
      <span>2</span><span>3</span><span>4</span><span>5</span><span>6</span><span>7</span><span>8</span>
      <span>9</span><span>10</span><span>11</span><span>12</span><span>13</span><span class="event">14</span><span>15</span>
      <span>16</span><span>17</span><span class="today">18</span><span>19</span><span>20</span><span class="marked">21</span><span>22</span>
      <span>23</span><span>24</span><span>25</span><span>26</span><span>27</span><span>28</span><span>29</span>
      <span>30</span><span class="muted">1</span><span class="muted">2</span><span class="muted">3</span><span class="muted">4</span><span class="muted">5</span><span class="muted">6</span>
    </div>
  </div>

  <div class="countdown">
    <div class="countdown-inner">
      <div class="digit" style="left:10px">05</div>
      <span class="colon" style="left:83px">:</span>
      <div class="digit" style="left:96px">24</div>
      <span class="colon" style="left:169px">:</span>
      <div class="digit" style="left:182px">36</div>
    </div>
  </div>
  <div class="count-labels">
    <span style="left:844px">Hours</span>
    <span style="left:930px">Minutes</span>
    <span style="left:1018px">Seconds</span>
  </div>

  <footer class="site-footer">
    <div class="footer-links" style="top:18px">
      <a href="#">Home</a><i>:</i><a href="#">About Us</a><i>:</i><a href="#">Courses &amp; Prices</a><i>:</i><a href="#">Contact Us</a><i>:</i><a href="#">FAQ</a><i>:</i><a href="#">Calendar</a><i>:</i><a href="#">Privacy Policy</a><i>:</i><a href="#">Sitemap</a>
    </div>
    <div class="footer-links" style="top:36px">
      <a href="#">Try a Dive Evening</a><i>:</i><a href="#">Scuba Review</a><i>:</i><a href="#">Beginners Course</a><i>:</i><a href="#">Advanced Open water</a><i>:</i><a href="#">Rescue Diver</a><i>:</i><a href="#">DiveMaster Course</a>
    </div>
    <div class="copyright">Copyright © FinWaveX 2013. All rights reserved.</div>
    <a class="social" style="left:978px" href="#" aria-label="Social link"></a>
    <a class="social" style="left:1016px" href="#" aria-label="Social link"></a>
    <a class="social" style="left:1054px" href="#" aria-label="Social link"></a>
    <a class="social" style="left:1091px" href="#" aria-label="Feed link"></a>
  </footer>
</div>
</body>
</html>
```